Norvale Structural Approval Standards Private Assessors

Professional Construction Consultancy Company Business Card - must keep logo colours see images below - examples have been added from my last competition - please see them as examples only!

Target Market(s)

Home Builders

Industry/Entity Type

Construction

Contact Information for Business Card

See "must haves"

Font styles to use
Sans Serif

Colors
ffffff
add136
000000

Requirements
Must have
• Daniel Moravi
• Director
• Phone: 0491 570 156
• Address: 7 Tarrunga Rd,
• Hallworth Vale, SA, 5091
• Email: norvaleassessors@mailbox-example.com
• Website: www.norvaleassessors-example.com.au
• Facebook: Norvale Structural Approval Standards
Nice to have
• Side 1: full logo
• Side 2: company details
Should not have
• hard to read
• must be clear and professional

```html
<!DOCTYPE html>
<html lang="en">
<head>
<meta charset="utf-8">
<title>Norvale Structural Approval Standards – Business Card</title>
<link rel="stylesheet" href="https://fonts.googleapis.com/css2?family=Open+Sans:wght@400;600;700&display=swap">
<style>
  :root {
    --lime: #add136;
    --ink: #000000;
    --card: #0b0b0b;
    --paper: #ffffff;
    --backdrop: #4a413c;
  }
  * { box-sizing: border-box; margin: 0; padding: 0; }
  html, body {
    width: 1200px; height: 900px; overflow: hidden;
    background: var(--backdrop);
    font-family: "Open Sans", Arial, sans-serif;
  }
  .canvas {
    width: 1200px; height: 900px;
    display: flex; align-items: center; justify-content: center; gap: 60px;
  }
  .card {
    width: 525px; height: 300px;
    background: var(--card);
    border-radius: 4px;
    box-shadow: 0 10px 30px rgba(0,0,0,.45);
    position: relative;
    overflow: hidden;
  }

  /* Contact side */
  .card--details { display: flex; align-items: center; padding: 0 30px; }
  .brand-block {
    width: 150px; flex: none; display: flex; align-items: center; gap: 10px;
  }
  .brand-mark { width: 14px; height: 14px; background: var(--lime); flex: none; }
  .brand-name {
    color: var(--lime); font-weight: 700; font-size: 18px; line-height: 1.15;
  }
  .divider { width: 1px; height: 170px; background: var(--lime); opacity: .7; margin: 0 20px 0 12px; flex: none; }
  .details { color: var(--paper); font-size: 12.5px; line-height: 1.4; white-space: nowrap; }
  .person-name { color: var(--lime); font-weight: 700; font-size: 15px; }
  .person-role { font-size: 12px; margin-bottom: 14px; }
  .address { margin-bottom: 14px; }
  .contact-list { list-style: none; }
  .contact-list li { display: flex; align-items: center; gap: 8px; }
  .contact-list svg { width: 10px; height: 10px; flex: none; fill: var(--lime); }

  /* Logo side */
  .card--logo { display: flex; align-items: center; justify-content: center; }
  .logo-lockup { display: flex; align-items: center; gap: 16px; }
  .logo-mark { width: 26px; height: 26px; background: var(--lime); flex: none; }
  .logo-name {
    color: var(--lime); font-weight: 700; font-size: 28px; line-height: 1.12;
  }
</style>
</head>
<body>
<main class="canvas">
  <section class="card card--details" aria-label="Business card, contact side">
    <div class="brand-block">
      <span class="brand-mark"></span>
      <span class="brand-name">Norvale<br>Structural<br>Approval<br>Standards</span>
    </div>
    <div class="divider"></div>
    <div class="details">
      <p class="person-name">Daniel Moravi</p>
      <p class="person-role">Director</p>
      <p class="address">7 Tarrunga Rd,<br>Hallworth Vale, SA, 5091</p>
      <ul class="contact-list">
        <li><svg viewBox="0 0 10 10"><path d="M2 0.5 L3.6 0.5 L4.2 2.8 L3.1 3.6 Q4 5.9 6.4 6.9 L7.2 5.8 L9.5 6.4 L9.5 8 Q9.2 9.5 7.8 9.5 Q1 8.8 0.5 2.2 Q0.5 0.8 2 0.5 Z"/></svg>0491 570 156</li>
        <li><svg viewBox="0 0 10 10"><path d="M0.5 2 H9.5 V8.5 H0.5 Z M1 2.4 L5 5.6 L9 2.4" stroke="#0b0b0b" stroke-width="0.8"/></svg>norvaleassessors@mailbox-example.com</li>
        <li><svg viewBox="0 0 10 10"><circle cx="5" cy="5" r="4.5"/><path d="M0.5 5 H9.5 M5 0.5 Q2.5 5 5 9.5 M5 0.5 Q7.5 5 5 9.5" stroke="#0b0b0b" stroke-width="0.7" fill="none"/></svg>www.norvaleassessors-example.com.au</li>
        <li><svg viewBox="0 0 10 10"><circle cx="5" cy="5" r="4.5"/></svg>Norvale Structural Approval Standards</li>
      </ul>
    </div>
  </section>

  <section class="card card--logo" aria-label="Business card, logo side">
    <div class="logo-lockup">
      <span class="logo-mark"></span>
      <span class="logo-name">Norvale Structural<br>Approval Standards<br>Private Assessors</span>
    </div>
  </section>
</main>
</body>
</html>
```